IT Services Business Card Design

We require a business card design for an IT services company called RT Code Transit.

We specialize in taking an organisations software and readying it for deployment to new environments (e.g. Nex 3 to Nex 5). This process is termed application packaging. This is not the same as putting things in boxes but I am happy to use boxes as a pun icon ;-) This is our second step in branding, we currently have a new logo and our poor excuse of a website is next to be updated but it contains information on who we are and what we cover at rtcodetransit.example

We are looking for a fun, modern but stylish and professional looking design.

I have attached the logo in multiple formats including vector formats (and the fonts that created the logo if required)
Updates

Thanks to all the designers so far, some great designs in there.  I will be selecting a card design on the deadline date. 

However, there is still time to submit some more designs.  The majority of the ones I have so far are typical simplistic designs that we have all seen before and I have enough of those to choose from now.  If you wish to submit any more designs, please submit somthing unusual to grab our attention.

Target Market(s)

Project executives of large organisations looking for Nexora migrations

Industry/Entity Type

Software

Requirements
Must have
• Want to show company name, contact name, title, main number, contact number, fax number, email address and website address. I do not want to show the address.
Must use the attached logo, retaining the colours in them.

This has to be a double-sided design. I will be using pelby.example and will be selecting their rounded corner business card design.

Their templates and design requirements (sizing etc.) can be found here: http://uk.pelby.example/help/faq/templates-and-guidelines.html

Happy for company name or website to be on either side of the card.

This design has to be original and not used before for another company

Would like to style it around the business colours in the logo
Nice to have
• Pelby.example has an option for multiple card designs to appear on the back. If this is possible in the budget and time you have and you have a design(s) that work with that but carry the same style and theme, that would be nice to see but not necessary.
Should not have
• We do not want to put a postal address on the cards

```html
<!DOCTYPE html>
<html lang="en">
<head>
<meta charset="utf-8">
<title>RT Code Transit — Business Card</title>
<link rel="stylesheet" href="https://fonts.googleapis.com/css2?family=Jost:wght@300;400&display=swap">
<style>
  :root {
    --backdrop: #e4e2df;
    --card-white: #ffffff;
    --card-dark: #3a3a3b;
    --ink-grey: #5b5b5d;
    --ink-dark: #333335;
    --ink-light: #c9c9cb;
    --brand-blue: #4a6fdc;
    --card-radius: 22px;
  }
  * { box-sizing: border-box; margin: 0; padding: 0; }
  html, body {
    width: 1200px;
    height: 787px;
    overflow: hidden;
    background: var(--backdrop);
    font-family: "Jost", "Century Gothic", sans-serif;
    font-weight: 300;
  }
  .canvas {
    width: 1200px;
    height: 787px;
    display: flex;
    align-items: center;
    justify-content: center;
    gap: 40px;
  }
  .card {
    position: relative;
    width: 520px;
    height: 336px;
    border-radius: var(--card-radius);
    box-shadow: 0 10px 28px rgba(0,0,0,0.18);
    overflow: hidden;
  }
  .card--front { background: var(--card-white); color: var(--ink-dark); }
  .card--back { background: var(--card-dark); color: var(--ink-light); }

  .brand {
    position: absolute;
    display: flex;
    align-items: center;
    gap: 14px;
  }
  .brand__dot {
    flex: none;
    border-radius: 50%;
    background: var(--brand-blue);
  }
  .brand__name {
    font-weight: 300;
    letter-spacing: 0.02em;
    white-space: nowrap;
  }
  .card--front .brand { left: 56px; top: 52px; }
  .card--front .brand__dot { width: 34px; height: 34px; }
  .card--front .brand__name { font-size: 34px; color: var(--ink-grey); }

  .person {
    position: absolute;
    left: 56px;
    top: 138px;
  }
  .person__name { font-size: 24px; color: var(--ink-dark); }
  .person__title {
    font-size: 11px;
    letter-spacing: 0.12em;
    color: var(--ink-grey);
    margin-top: 2px;
  }

  .contact {
    position: absolute;
    left: 232px;
    top: 200px;
    font-size: 14px;
    line-height: 1.45;
    color: var(--ink-dark);
  }
  .contact__row { display: flex; gap: 10px; }
  .contact__label { width: 12px; font-size: 11px; color: var(--ink-grey); padding-top: 2px; }
  .contact__web { color: var(--brand-blue); margin-top: 4px; }

  .card--back .brand { left: 56px; top: 62px; }
  .card--back .brand__name { font-size: 36px; color: var(--ink-light); }
  .card--back .brand__dot {
    position: absolute;
    width: 210px;
    height: 210px;
    right: -40px;
    bottom: -60px;
  }
</style>
</head>
<body>
  <main class="canvas">
    <section class="card card--front" aria-label="Card front">
      <div class="brand">
        <span class="brand__dot"></span>
        <span class="brand__name">RT Code Transit</span>
      </div>
      <div class="person">
        <p class="person__name">Dana Whitfield</p>
        <p class="person__title">DIRECTOR</p>
      </div>
      <div class="contact">
        <p class="contact__row"><span class="contact__label">T</span><span>(555) 014-2270</span></p>
        <p class="contact__row"><span class="contact__label">M</span><span>(555) 014-2270</span></p>
        <p class="contact__row"><span class="contact__label">F</span><span>(555) 014-2270</span></p>
        <p class="contact__row"><span class="contact__label"></span><span>dana@rtcodetransit.example</span></p>
        <p class="contact__row contact__web"><span class="contact__label"></span><span>www.rtcodetransit.example</span></p>
      </div>
    </section>

    <section class="card card--back" aria-label="Card back">
      <span class="brand__dot"></span>
      <div class="brand">
        <span class="brand__name">RT Code Transit</span>
      </div>
    </section>
  </main>
</body>
</html>
```